Business cards for KORBEN Real Estate Properties LLC

We need a cool, original business card design for a company based in the Washington DC metropolitan area. We are a new energetic and passionate Real Estate Investing Company that invests in all types of real estate; commercial, residential, industrial etc.

Our company color is Red since it reflects action, energy and speed; it is assertive confident, energizing, exciting, powerful, passionate and determined. So we would like business card communicate those qualities to the audience.

Our audiences are investors that want to invest with us, real estate sellers, buyers, and tenants who lease from us.

Our logo is attached

```html
<!DOCTYPE html>
<html lang="en">
<head>
<meta charset="utf-8">
<title>KORBEN Real Estate Properties LLC – Business Cards</title>
<link href="https://fonts.googleapis.com/css2?family=Montserrat:wght@400;600;700&family=Open+Sans:wght@400;600&display=swap" rel="stylesheet">
<style>
  :root {
    --page: #e9e7e4;
    --charcoal: #1f1f21;
    --charcoal-2: #2c2c2f;
    --slate: #4a4a4e;
    --steel: #6b6b70;
    --silver: #cfcfd1;
    --silver-2: #b5b5b8;
    --red: #d4152a;
    --red-dark: #9e0d1d;
    --white: #ffffff;
  }
  * { box-sizing: border-box; margin: 0; padding: 0; }
  html, body { width: 704px; height: 1200px; overflow: hidden; }
  body {
    background: var(--page);
    font-family: "Open Sans", Arial, sans-serif;
    position: relative;
  }
  .card {
    position: absolute;
    left: 72px;
    width: 560px;
    height: 320px;
    border-radius: 18px;
    overflow: hidden;
    box-shadow: 0 10px 28px rgba(0,0,0,.22);
  }
  .card-front { top: 140px; background: var(--charcoal); }
  .card-back  { top: 740px; background: var(--silver); }
  .card-art { position: absolute; inset: 0; width: 100%; height: 100%; }

  .brand { position: absolute; display: flex; align-items: center; gap: 14px; }
  .brand-dot { width: 22px; height: 22px; border-radius: 50%; background: var(--red); flex: none; }
  .brand-name {
    font-family: "Montserrat", Arial, sans-serif;
    font-weight: 600;
    line-height: 1.05;
    text-transform: uppercase;
  }
  .brand-name .big { display: block; font-size: 52px; letter-spacing: 2px; }
  .brand-name .small { display: block; font-size: 14.5px; letter-spacing: 1px; margin-top: 4px; }

  .card-front .brand { left: 70px; top: 112px; }
  .card-front .brand-name { color: var(--white); }

  .card-back .brand { left: 40px; top: 40px; }
  .card-back .brand-name { color: var(--slate); }
  .card-back .brand-name .big { font-size: 44px; }
  .card-back .brand-name .small { font-size: 12.5px; }

  .contacts {
    position: absolute;
    left: 40px;
    top: 178px;
    list-style: none;
    color: var(--white);
    font-size: 12.5px;
    line-height: 19px;
  }
  .contacts li { display: flex; align-items: center; gap: 10px; }
  .contacts .icon { width: 9px; height: 9px; background: var(--red); border-radius: 2px; flex: none; }

  .person {
    position: absolute;
    right: 150px;
    top: 190px;
    text-align: right;
    color: var(--white);
  }
  .person-name { font-family: "Montserrat", Arial, sans-serif; font-weight: 700; font-size: 19px; }
  .person-title { font-size: 13px; }
</style>
</head>
<body>

  <section class="card card-front" aria-label="Business card front">
    <svg class="card-art" viewBox="0 0 560 320" aria-hidden="true">
      <defs>
        <linearGradient id="front-bg" x1="0" y1="0" x2="1" y2="1">
          <stop offset="0" stop-color="#2e2e31"/>
          <stop offset="1" stop-color="#151516"/>
        </linearGradient>
      </defs>
      <rect width="560" height="320" fill="url(#front-bg)"/>
      <polygon points="330,0 560,0 560,120" fill="#3a3a3e"/>
      <polygon points="400,0 560,0 560,60" fill="#55555a"/>
      <polygon points="430,320 560,190 560,320" fill="#2a2a2d"/>
      <polygon points="470,320 560,240 560,320" fill="#5d5a5a"/>
    </svg>
    <div class="brand">
      <span class="brand-dot"></span>
      <span class="brand-name">
        <span class="big">KORBEN</span>
        <span class="small">Real Estate Properties LLC</span>
      </span>
    </div>
  </section>

  <section class="card card-back" aria-label="Business card back">
    <svg class="card-art" viewBox="0 0 560 320" aria-hidden="true">
      <defs>
        <linearGradient id="back-bg" x1="0" y1="0" x2="1" y2="0">
          <stop offset="0" stop-color="#d8d8da"/>
          <stop offset="1" stop-color="#b9b9bc"/>
        </linearGradient>
      </defs>
      <rect width="560" height="320" fill="url(#back-bg)"/>
      <polygon points="0,160 560,140 560,320 0,320" fill="var(--slate)"/>
      <rect x="0" y="300" width="560" height="20" fill="var(--red)"/>
      <rect x="0" y="296" width="560" height="4" fill="var(--red-dark)"/>
      <g stroke="var(--white)" stroke-width="7" stroke-linecap="square">
        <line x1="470" y1="290" x2="540" y2="150"/>
        <line x1="492" y1="290" x2="552" y2="170"/>
        <line x1="514" y1="290" x2="560" y2="198"/>
      </g>
    </svg>
    <div class="brand">
      <span class="brand-dot"></span>
      <span class="brand-name">
        <span class="big">KORBEN</span>
        <span class="small">Real Estate Properties LLC</span>
      </span>
    </div>
    <ul class="contacts">
      <li><span class="icon"></span>0123 456 789</li>
      <li><span class="icon"></span>0123 456 789</li>
      <li><span class="icon"></span>0123 456 789</li>
      <li><span class="icon"></span>youremail@email.com</li>
      <li><span class="icon"></span>www.yourwebsite.com</li>
    </ul>
    <div class="person">
      <div class="person-name">Your Name</div>
      <div class="person-title">Your title</div>
    </div>
  </section>

</body>
</html>
```